Innovative cost reduction consultant needs to build a group of technical advisors

We need to share our message and compassion for developing cost reduction in the automotive industry. We create opportunities for immediate innovation, by developing cost reduction solutions across suppliers with related process. Attached is an existing Power Point, but it needs improvement. Most of all, a good compelling story, why experts should join us.

Target Market(s)

Automotive industry, supply chain management

Industry/Entity Type

Automotive

Font styles to use
Serif
Sans Serif

Requirements
Must have
• Better visual graphics. There are a few, but they are not as visually appearing as I would like. A graphic with data should have a better visual impact then the ones that I created. I would like to share the message, that I am providing a solution for the automotive industry. The goal is to reduce costs and improve supplier and OEM relationships. The objective is to do so by creating opportunities for immediate innovation, by developing cost reduction solutions across suppliers with related processes. This message may need a visual graphic, which is missing from the presentation.
Nice to have
• Challenge my story and presentation. Does this make sense to you, and what is your opinions of the subject. Or, a relevant news source to validate the story.
Should not have
• I have not decided on the name of the venture or logo. So, let's just use my name as the source or writer. Marcus Trevell, Cost Reduction Specialist. Thanks,

```html
<!DOCTYPE html>
<html lang="en">
<head>
<meta charset="UTF-8">
<title>Case Study – Supplier Cost Reduction</title>
<link rel="stylesheet" href="https://fonts.googleapis.com/css2?family=Anton&family=Roboto+Condensed:wght@400;700&display=swap">
<style>
  :root {
    --brand-blue: #1a9ee0;
    --red-bright: #e3001b;
    --red-deep: #b0101c;
    --green-deep: #0f5a2a;
    --green-bright: #1c8a3c;
    --brown-mid: #6b3a1e;
    --brown-deep: #3b2114;
    --ring-grey: #cfcfcf;
    --shadow-grey: #e4e4e4;
    --badge-black: #120606;
    --text-dark: #3a3a3a;
    --white: #ffffff;
    --panel-grey: #cdcdcd;
  }
  html, body {
    margin: 0;
    padding: 0;
    overflow: hidden;
  }
  .slide {
    position: relative;
    width: 1200px;
    height: 650px;
    overflow: hidden;
    background: linear-gradient(90deg, var(--white) 0%, var(--white) 50%, #ececec 75%, var(--panel-grey) 100%);
    font-family: "Roboto Condensed", "Arial Narrow", sans-serif;
  }
  .footer-band {
    position: absolute;
    left: 0;
    bottom: 0;
    width: 1200px;
    height: 28px;
    background: var(--brand-blue);
  }
  .case-graphic {
    position: absolute;
    left: 0;
    top: 0;
    width: 1200px;
    height: 650px;
  }
  .case-title {
    font-family: "Anton", "Impact", sans-serif;
    font-size: 46px;
    fill: var(--brand-blue);
    stroke: var(--white);
    stroke-width: 2px;
    paint-order: stroke;
    letter-spacing: 1px;
  }
  .badge-figure {
    font-family: "Roboto Condensed", "Arial Narrow", sans-serif;
    font-weight: 700;
    font-size: 27px;
    fill: var(--white);
  }
  .segment-label {
    font-family: "Roboto Condensed", "Arial Narrow", sans-serif;
    font-weight: 700;
    font-size: 12.5px;
    fill: var(--white);
  }
  .goal-list {
    position: absolute;
    left: 706px;
    top: 272px;
    margin: 0;
    padding: 0;
    list-style: none;
    color: var(--text-dark);
    font-size: 19px;
  }
  .goal-list li {
    position: relative;
    padding-left: 22px;
    height: 34px;
    line-height: 28px;
  }
  .goal-list li::before {
    content: "";
    position: absolute;
    left: 0;
    top: 7px;
    border-left: 9px solid var(--brand-blue);
    border-top: 6px solid transparent;
    border-bottom: 6px solid transparent;
  }
</style>
</head>
<body>
<div class="slide">
  <svg class="case-graphic" viewBox="0 0 942 510" xmlns="http://www.w3.org/2000/svg">
    <defs>
      <radialGradient id="badgeGlowRed" cx="50%" cy="50%" r="50%">
        <stop offset="70%" stop-color="var(--badge-black)"/>
        <stop offset="100%" stop-color="#7a0a10"/>
      </radialGradient>
      <radialGradient id="badgeGlowGreen" cx="50%" cy="50%" r="50%">
        <stop offset="70%" stop-color="#06140a"/>
        <stop offset="100%" stop-color="#1f6b35"/>
      </radialGradient>
      <radialGradient id="badgeGlowBrown" cx="50%" cy="50%" r="50%">
        <stop offset="70%" stop-color="#140a05"/>
        <stop offset="100%" stop-color="#5a3219"/>
      </radialGradient>
      <radialGradient id="regionFill" cx="50%" cy="48%" r="55%">
        <stop offset="0%" stop-color="#1a9ee0"/>
        <stop offset="70%" stop-color="#4db4ea"/>
        <stop offset="100%" stop-color="#ffffff"/>
      </radialGradient>
      <path id="titleArc" d="M166.7 93.5 A205 205 0 0 1 419.3 93.5"/>
    </defs>

    <!-- soft base shadow -->
    <circle cx="296" cy="262" r="197" fill="var(--shadow-grey)"/>

    <!-- red segment -->
    <path d="M101 255 A192 192 0 0 1 164.6 112.3 L218.1 171.8 A112 112 0 0 0 181 255 Z" fill="var(--red-bright)" stroke="var(--white)" stroke-width="2"/>
    <path d="M157.2 390.8 A192 192 0 0 1 101 255 L181 255 A112 112 0 0 0 213.8 334.2 Z" fill="var(--red-deep)" stroke="var(--white)" stroke-width="2"/>

    <!-- green segment -->
    <path d="M421.4 112.3 A192 192 0 0 1 485 255 L405 255 A112 112 0 0 0 367.9 171.8 Z" fill="var(--green-deep)" stroke="var(--white)" stroke-width="2"/>
    <path d="M485 255 A192 192 0 0 1 428.8 390.8 L372.2 334.2 A112 112 0 0 0 405 255 Z" fill="var(--green-bright)" stroke="var(--white)" stroke-width="2"/>

    <!-- brown segment -->
    <path d="M428.8 390.8 A192 192 0 0 1 293 447 L293 367 A112 112 0 0 0 372.2 334.2 Z" fill="var(--brown-deep)" stroke="var(--white)" stroke-width="2"/>
    <path d="M293 447 A192 192 0 0 1 157.2 390.8 L213.8 334.2 A112 112 0 0 0 293 367 Z" fill="var(--brown-mid)" stroke="var(--white)" stroke-width="2"/>

    <!-- centre ring and region -->
    <circle cx="293" cy="255" r="100" fill="var(--white)"/>
    <circle cx="293" cy="255" r="94" fill="none" stroke="var(--ring-grey)" stroke-width="9"/>
    <circle cx="293" cy="255" r="80" fill="url(#regionFill)" role="img" aria-label="Map of the eastern and central United States supplier region"/>

    <!-- title -->
    <text class="case-title" text-anchor="middle">
      <textPath href="#titleArc" startOffset="50%">CASE STUDY</textPath>
    </text>

    <!-- badges -->
    <g class="badge">
      <circle cx="168" cy="180" r="33" fill="url(#badgeGlowRed)" stroke="#5a0a0e" stroke-width="2"/>
      <text class="badge-figure" x="168" y="190" text-anchor="middle">47</text>
    </g>
    <g class="badge">
      <circle cx="440" cy="178" r="33" fill="url(#badgeGlowGreen)" stroke="#0a3a1a" stroke-width="2"/>
      <text class="badge-figure" x="440" y="188" text-anchor="middle">$3</text>
    </g>
    <g class="badge">
      <circle cx="237" cy="392" r="33" fill="url(#badgeGlowBrown)" stroke="#2a150a" stroke-width="2"/>
      <text class="badge-figure" x="237" y="402" text-anchor="middle">$95</text>
    </g>

    <!-- segment labels -->
    <text class="segment-label" text-anchor="middle">
      <tspan x="150" y="276">Automotive</tspan>
      <tspan x="150" y="292">suppliers,</tspan>
      <tspan x="150" y="308">NAFTA</tspan>
    </text>
    <text class="segment-label" text-anchor="middle">
      <tspan x="436" y="280">Billion dollar</tspan>
      <tspan x="436" y="296">supplier base</tspan>
    </text>
    <text class="segment-label" text-anchor="middle">
      <tspan x="356" y="372">Million dollar</tspan>
      <tspan x="356" y="388">required annual</tspan>
      <tspan x="356" y="404">cost reduction</tspan>
    </text>
  </svg>

  <ul class="goal-list">
    <li>Re–build Automaker/Supplier relations</li>
    <li>Build on supplier group strengths</li>
    <li>Create collaborative efforts</li>
  </ul>

  <div class="footer-band"></div>
</div>
</body>
</html>
```